Copperleaf Vantage Training PowerPoint Template

I want to PowerPoint template theme using my attached logo. My colors are black and orange. My website is CopperleafVantage.com. I am a handgun training company.

Font:

- Serpentine-Bold-Bold for "IRON BRAE"

- BrowalliaUPC for "SHOOTING SPORTS"

Colors (CMYK code):

- BLACK ....... 0; 0; 0; 100;
- ORANGE ... gradient from 0; 65; 97.5; 0 to 0; 39; 97.5; 0

```html
<!DOCTYPE html>
<html lang="en">
<head>
<meta charset="utf-8">
<title>Copperleaf Vantage Training – Title Slide</title>
<link rel="stylesheet" href="https://fonts.googleapis.com/css2?family=Russo+One&family=Arimo:wght@400&display=swap">
<style>
  :root {
    --bg-top: #1c1f22;
    --bg-bottom: #15171a;
    --band-light: #2c3034;
    --white: #ffffff;
    --text-soft: #f2f2f2;
    --orange-start: #f26b0f;
    --orange-end: #f9aa0b;
  }
  * { margin: 0; padding: 0; box-sizing: border-box; }
  html, body { width: 1200px; height: 900px; overflow: hidden; background: var(--bg-bottom); }
  .slide {
    position: relative;
    width: 1200px;
    height: 900px;
    overflow: hidden;
    background: linear-gradient(180deg, var(--bg-top) 0%, #191c1f 51%, var(--bg-bottom) 52%, var(--bg-bottom) 100%);
  }
  .slide__band {
    position: absolute;
    left: 0; top: 460px;
    width: 1200px; height: 40px;
    background: linear-gradient(180deg, var(--band-light) 0%, rgba(44,48,52,0) 100%);
    border-top: 1px solid #34383d;
  }
  .brand {
    position: absolute;
    left: 222px; top: 322px;
    display: flex;
    align-items: center;
    gap: 34px;
  }
  .brand__mark {
    width: 150px; height: 150px;
    background: linear-gradient(135deg, var(--orange-start), var(--orange-end));
  }
  .brand__name {
    font-family: "Russo One", sans-serif;
    font-size: 50px;
    line-height: 1.1;
    color: var(--white);
    text-transform: uppercase;
  }
  .title-block {
    position: absolute;
    left: 0; top: 550px;
    width: 1200px;
    text-align: center;
  }
  .title-block__heading {
    font-family: "Russo One", sans-serif;
    font-size: 60px;
    line-height: 1;
    color: var(--white);
    letter-spacing: 1px;
  }
  .title-block__sub {
    margin-top: 32px;
    font-family: "Arimo", sans-serif;
    font-size: 21px;
    line-height: 42px;
    color: var(--text-soft);
    letter-spacing: 0.5px;
  }
  .footer-bar {
    position: absolute;
    left: 0; bottom: 0;
    width: 1200px; height: 75px;
    background: linear-gradient(90deg, var(--orange-start) 0%, var(--orange-end) 100%);
  }
</style>
</head>
<body>
  <main class="slide">
    <div class="slide__band"></div>

    <div class="brand">
      <div class="brand__mark"></div>
      <div class="brand__name">Copperleaf Vantage<br>Training</div>
    </div>

    <section class="title-block">
      <h1 class="title-block__heading">PROJECT TITLE HERE</h1>
      <p class="title-block__sub">SUB TEXT HERE SUB TEXT HERE SUB TEXT HERE<br>SUB TEXT HERE SUB TEXT HERE</p>
    </section>

    <div class="footer-bar"></div>
  </main>
</body>
</html>
```